Non-Fiction Book On Creativity - Cover Design / Physical and E-Book

I am looking for designs for my first book! It's called: Patience Builds Harbors. The subtitle is: 12 Chapters About Gathering Courage, Mending Fences, And Walking A Quiet Road.
It's a series of short lessons and principals on creativity and it will be a Vellora book and a physical book.
I'm really open to any type of designs but have attached some screenshots of other book covers that have a design and style that I like.
Please let me know if you have any questions or need any more information.
Creativity / Self-Help / Personal Development

```html
<!DOCTYPE html>
<html lang="en">
<head>
<meta charset="utf-8">
<title>Patience Builds Harbors — Book Cover</title>
<link rel="stylesheet" href="https://fonts.googleapis.com/css2?family=Barlow+Condensed:wght@500&family=Barlow:wght@500&family=Playfair+Display:wght@400&family=Montserrat:wght@400&display=swap">
<style>
  :root {
    --backdrop: #b5b6b1;
    --paper: #ffffff;
    --navy: #083a63;
    --title-red: #a8191f;
    --subtitle-blue: #1c4f7a;
    --ink: #1e1e1e;
    --art-light: #f3f3f0;
    --art-warm: #fbf6da;
  }
  * { margin: 0; padding: 0; box-sizing: border-box; }
  html, body {
    width: 1200px;
    height: 1000px;
    overflow: hidden;
    background: var(--backdrop);
  }
  .canvas {
    position: relative;
    width: 1200px;
    height: 1000px;
    background: var(--backdrop);
  }
  .cover {
    position: absolute;
    left: 266px;
    top: 0;
    width: 667px;
    height: 1000px;
    background: var(--paper);
    overflow: hidden;
  }
  .cover-art {
    position: absolute;
    left: 138px;
    top: 30px;
    width: 470px;
    height: 332px;
    background: linear-gradient(180deg, var(--art-warm) 0%, var(--art-light) 100%);
    border-radius: 120px 120px 0 0;
  }
  .equation-band {
    position: absolute;
    left: 0;
    top: 362px;
    width: 100%;
    height: 285px;
    background: var(--navy);
    display: flex;
    align-items: center;
    justify-content: space-between;
    padding: 0 92px 0 96px;
  }
  .equation-letter {
    font-family: "Barlow Condensed", "Arial Narrow", sans-serif;
    font-weight: 500;
    font-size: 318px;
    line-height: 1;
    color: var(--paper);
    margin-top: 6px;
  }
  .equation-sign {
    width: 160px;
    height: 84px;
  }
  .title {
    position: absolute;
    left: 0;
    top: 655px;
    width: 100%;
    text-align: center;
    font-family: "Playfair Display", "Didot", serif;
    font-weight: 400;
    font-size: 66px;
    line-height: 68px;
    letter-spacing: 1px;
    color: var(--title-red);
    text-transform: uppercase;
  }
  .subtitle {
    position: absolute;
    left: 0;
    top: 875px;
    width: 100%;
    text-align: center;
    font-family: "Montserrat", "Helvetica", sans-serif;
    font-size: 14.5px;
    line-height: 22px;
    letter-spacing: 0.6px;
    color: var(--subtitle-blue);
    text-transform: uppercase;
  }
  .author {
    position: absolute;
    left: 0;
    top: 942px;
    width: 100%;
    text-align: center;
    font-family: "Barlow", "Helvetica", sans-serif;
    font-weight: 500;
    font-size: 22px;
    letter-spacing: 2.5px;
    color: var(--ink);
    text-transform: uppercase;
  }
</style>
</head>
<body>
  <main class="canvas">
    <section class="cover">
      <div class="cover-art" role="img" aria-label="Line drawing of a hand lifting the open top of a head and placing a yellow star inside it, with eyes glancing upward"></div>

      <div class="equation-band" aria-label="P equals H">
        <span class="equation-letter">P</span>
        <svg class="equation-sign" viewBox="0 0 160 84" aria-hidden="true">
          <rect x="0" y="0" width="160" height="25" fill="#ffffff"/>
          <rect x="0" y="59" width="160" height="25" fill="#ffffff"/>
        </svg>
        <span class="equation-letter">H</span>
      </div>

      <h1 class="title">Patience<br>Builds<br>Harbors</h1>

      <p class="subtitle">12 Chapters About Gathering Courage, Mending Fences,<br>And Walking A Quiet Road.</p>

      <p class="author">Author’s Name</p>
    </section>
  </main>
</body>
</html>
```